Banner for Vet Hospital 5m x 1.2m - Heat Stroke

Maplecourt Pet Hospital needs a Heat Stroke Banner for Summer.
The banner will be 5000mm long and 1200mm tall.

Our region has been hot this year and this summer is going to be extremely hot.
I want to warn people about heat stroke.
I want you to create a heat stroke banner that conveys the symptoms of heat stroke.

Pictures are better than words.
There should be IMAGES and WORDS that can be seen from the road 30m away and maybe some smaller words for people to read as they walk past.

Here are some of the signs of Heat Stroke:
- Panting which increases as heatstroke progresses
- Drooling, salivating
- Agitation, restlessness
- Very red or pale gums
- Bright red tongue
- Increased heart rate
- Breathing distress
- Vomiting Diarrhea (possibly with blood)
- Signs of mental confusion, delirium
- Dizziness, staggering
- Lethargy, weakness
- Muscle tremors
- Seizures
- Collapsing and lying down
- Little to no urine production
- Coma

I have attached characters that we often use in our advertising. They are optional.
I have done a mock up of the design I imagine. You could refine this design or make your own....or both.

Target Market(s)

Women aged 20 to 50.

Industry/Entity Type

Veterinary

Font styles to use
Sans Serif

Colors
fbed22
f78f20
ec1f27
ffffff

Requirements
Must have
• Heat Stroke Symtpms.
• Heat Stroke Warning.
• Summer theme.
Nice to have
• Bright colours.

```html
<!DOCTYPE html>
<html lang="en">
<head>
<meta charset="utf-8">
<title>Maplecourt Pet Hospital – Heat Stroke Banner</title>
<link rel="stylesheet" href="https://fonts.googleapis.com/css2?family=Montserrat:wght@700;800;900&family=Titan+One&display=swap">
<style>
  :root {
    --yellow: #fbed22;
    --orange: #f78f20;
    --orange-deep: #ee6a1c;
    --red: #ec1f27;
    --white: #ffffff;
    --ink: #2a2019;
    --brown: #5b4234;
    --taupe: #9b8a7c;
    --taupe-light: #c9bdb2;
    --grass: #cfe6b9;
    --grass-light: #e4f1d7;
    --page: #eef0ea;
  }
  * { margin: 0; padding: 0; box-sizing: border-box; }
  html, body {
    width: 1200px; height: 392px; overflow: hidden;
    background: var(--page);
  }
  .banner {
    position: absolute; left: 0; top: 63px;
    width: 1200px; height: 266px;
    background: linear-gradient(180deg, var(--white) 0%, #f4f4f4 70%, #ececec 100%);
    overflow: hidden;
    font-family: "Montserrat", Arial, sans-serif;
  }
  .banner > * { position: absolute; }

  .wave { right: 0; top: 0; width: 310px; height: 200px; }
  .ground { left: 0; bottom: 0; width: 1200px; height: 80px; }

  .brand-panel {
    left: 7px; top: 2px; width: 243px; height: 253px;
    background: var(--white);
  }
  .brand-flag {
    position: absolute; left: 0; top: 0; width: 243px; height: 90px;
    background: var(--yellow);
    clip-path: polygon(0 0, 100% 0, 100% 74%, 50% 100%, 0 74%);
    display: flex; align-items: flex-start; justify-content: center;
    padding-top: 12px;
    font-weight: 800; font-size: 27px; line-height: 27px;
    color: var(--ink); text-align: center; letter-spacing: 0.5px;
  }
  .brand-name {
    position: absolute; left: 0; right: 0; top: 112px;
    text-align: center;
    font-weight: 800; font-size: 30px; line-height: 34px;
    color: var(--brown);
  }

  .title {
    left: 535px; top: 12px;
    font-family: "Titan One", "Arial Black", sans-serif;
    font-size: 50px; line-height: 56px; font-style: italic;
    color: var(--yellow);
    -webkit-text-stroke: 2px var(--red);
    paint-order: stroke fill;
    text-shadow: 0 3px 0 var(--orange-deep);
  }

  .illustration-sun {
    left: 387px; top: 4px; width: 112px; height: 98px;
    border-radius: 50%;
    background: radial-gradient(circle, var(--yellow) 0%, #fdd21e 45%, rgba(251,237,34,0.25) 70%, rgba(255,255,255,0) 72%);
  }
  .illustration-dog {
    background: linear-gradient(180deg, #a4877a 0%, #8a6c5f 100%);
    border-radius: 40% 40% 12% 12%;
    opacity: 0.85;
  }
  .dog-early { left: 396px; top: 103px; width: 112px; height: 147px; }
  .dog-mid { left: 650px; top: 98px; width: 161px; height: 161px; }
  .dog-late { left: 968px; top: 170px; width: 178px; height: 76px; border-radius: 45% 45% 30% 30%; }

  .symptom {
    display: flex; align-items: center; justify-content: center;
    text-align: center;
    font-weight: 800; font-size: 10px; line-height: 11px;
    color: var(--white);
    border-radius: 48% 52% 46% 54% / 55% 50% 50% 45%;
    box-shadow: 0 2px 2px rgba(0,0,0,0.15);
  }
  .symptom--red { background: var(--red); }
  .symptom--orange { background: var(--orange); }
  .symptom--deep { background: var(--orange-deep); }
  .symptom--taupe { background: var(--taupe-light); color: var(--brown); font-size: 11px; }
  .symptom--brown { background: var(--brown); font-size: 12px; }
  .symptom--mocha { background: var(--taupe); font-size: 12px; }

  .s-panting   { left: 326px; top: 89px;  width: 88px; height: 47px; }
  .s-agitation { left: 326px; top: 152px; width: 88px; height: 45px; font-size: 11px; }
  .s-drooling  { left: 507px; top: 85px;  width: 94px; height: 54px; }
  .s-breathing { left: 673px; top: 76px;  width: 76px; height: 40px; font-size: 9px; }
  .s-diarrhea  { left: 624px; top: 116px; width: 58px; height: 32px; font-size: 9px; }
  .s-confusion { left: 798px; top: 89px;  width: 76px; height: 41px; font-size: 9px; }
  .s-vomiting  { left: 811px; top: 152px; width: 76px; height: 45px; font-size: 9px; }
  .s-tremors   { left: 944px; top: 103px; width: 75px; height: 44px; font-size: 9px; }
  .s-collapse  { left: 1035px; top: 76px; width: 94px; height: 54px; }
  .s-coma      { left: 1108px; top: 129px; width: 78px; height: 45px; }

  .stage-arrow { width: 51px; height: 27px; }
  .arrow-one { left: 532px; top: 162px; }
  .arrow-two { left: 903px; top: 156px; }
</style>
</head>
<body>
  <div class="banner">
    <svg class="wave" viewBox="0 0 310 200" aria-hidden="true">
      <path d="M0 0 H310 V200 C290 150 260 120 200 95 C140 70 90 60 40 30 C20 18 8 8 0 0 Z" fill="var(--orange)"/>
      <path d="M60 0 H310 V120 C270 90 230 80 170 60 C120 45 90 25 60 0 Z" fill="var(--orange-deep)"/>
    </svg>
    <svg class="ground" viewBox="0 0 1200 80" preserveAspectRatio="none" aria-hidden="true">
      <path d="M0 60 C300 20 700 40 1200 10 V80 H0 Z" fill="var(--grass-light)"/>
      <path d="M0 70 C350 40 800 55 1200 30 V80 H0 Z" fill="var(--grass)"/>
    </svg>

    <div class="brand-panel">
      <div class="brand-flag">BOOK<br>ONLINE</div>
      <div class="brand-name">Maplecourt<br>Pet Hospital</div>
    </div>

    <div class="title">Heat Stroke</div>

    <div class="illustration-sun" role="img" aria-label="Bright cartoon summer sun"></div>

    <div class="illustration-dog dog-early" role="img" aria-label="Cartoon dog sitting and panting with tongue out"></div>
    <div class="illustration-dog dog-mid" role="img" aria-label="Cartoon dog drooling heavily and unwell"></div>
    <div class="illustration-dog dog-late" role="img" aria-label="Cartoon dog collapsed lying on the ground"></div>

    <div class="symptom symptom--red s-panting">EXCESSIVE<br>PAINTING</div>
    <div class="symptom symptom--orange s-agitation">AGITATION</div>
    <div class="symptom symptom--mocha s-drooling">DROOLING</div>
    <div class="symptom symptom--orange s-breathing">BREATHING<br>DISTRESS</div>
    <div class="symptom symptom--deep s-diarrhea">DIARRHEA</div>
    <div class="symptom symptom--deep s-confusion">CONFUSION</div>
    <div class="symptom symptom--taupe s-vomiting">VOMATING</div>
    <div class="symptom symptom--red s-tremors">MUSCLES<br>TREMORS</div>
    <div class="symptom symptom--brown s-collapse">COLLAPSE</div>
    <div class="symptom symptom--mocha s-coma">COMA</div>

    <svg class="stage-arrow arrow-one" viewBox="0 0 51 27" aria-hidden="true">
      <path d="M2 8 H30 V1 L49 13.5 L30 26 V19 H2 Z" fill="var(--white)" stroke="var(--brown)" stroke-width="2.5" stroke-linejoin="round"/>
    </svg>
    <svg class="stage-arrow arrow-two" viewBox="0 0 51 27" aria-hidden="true">
      <path d="M2 8 H30 V1 L49 13.5 L30 26 V19 H2 Z" fill="var(--white)" stroke="var(--brown)" stroke-width="2.5" stroke-linejoin="round"/>
    </svg>
  </div>
</body>
</html>
```